Tesk Laptop Cover Skin for a DJ

I’m a wedding/corporate DJ that’s looking to have a unique laptop skin design for my Zentrix laptop.

I will like to have a laptop cover skin that is a creative combination of professional, uniqueness, timeliness and looks solid.

I will like someone to take my current logo to incorporate into the design and only change the bottom “Tagline” in the logo to my new tagline listed below in the same area as the current tag.
New Tag: DJ Services | Photo Booths | Event Lighting

3D Feel
½ of laptop design with info list above and ½ laptop design with VTK attached logo
Colors: Stick with colors in my logo
Professional Design
o Note: I used this laptop for meetings and for DJ Gigs
Fonts: Open
Company Colors: Maroon / white / black

I have added our logo as an attachment, as well as our current laptop design skin. We are looking for something totally different.

Additionally, I have attached a further description of what we will like included.

Requirements
Must have
• Name: DoRN HaLE ( Name need to be BIG but not over bearing ) Company Name: VTK Entertainment 2nd Co Name: VTK Management Website: www.vtkentertainment-example.net VTK Logo Attached: See attached file o Note: EPS or AI file format of the logo can be sent to winner of the design contest PW Name: MrVTK7000 Hashtag: #VTKEntertainment Chatterly Name: VTK Entertainment

```html
<!DOCTYPE html>
<html lang="en">
<head>
<meta charset="utf-8">
<title>DoRN HaLE – Laptop Skin</title>
<link rel="stylesheet" href="https://fonts.googleapis.com/css2?family=Audiowide&family=Montserrat:wght@300;400;500;600;700&display=swap">
<style>
  :root {
    --maroon: #8a1a1a;
    --maroon-bright: #b81e24;
    --maroon-deep: #5a0d10;
    --black: #000000;
    --white: #ffffff;
    --page: #ffffff;
    --grey-soft: #d9d9d9;
  }
  * { box-sizing: border-box; margin: 0; padding: 0; }
  html, body {
    width: 1200px; height: 1071px; overflow: hidden;
    background: var(--page);
    font-family: "Montserrat", sans-serif;
  }
  .skin {
    position: absolute; left: 30px; top: 158px;
    width: 1140px; height: 754px;
    background: var(--black);
    border-radius: 28px;
    overflow: hidden;
  }
  .brand {
    position: absolute; left: 52px; top: 120px; width: 280px;
  }
  .brand-name {
    display: flex; align-items: center; gap: 10px;
    font-family: "Montserrat", sans-serif;
    font-weight: 700; font-size: 34px; line-height: 1;
    color: var(--maroon-bright);
  }
  .brand-dot {
    width: 22px; height: 22px; border-radius: 50%;
    background: var(--grey-soft); flex: none;
  }
  .brand-tagline {
    margin-top: 72px; margin-left: 47px;
    font-size: 10px; font-weight: 600; color: var(--white);
    white-space: nowrap;
  }
  .hero-art {
    position: absolute; left: 39px; top: 287px;
    width: 484px; height: 436px;
    background: linear-gradient(180deg, #1a0304 0%, #7d1417 55%, #a81c22 100%);
    border-radius: 6px;
  }
  .owner-name {
    position: absolute; left: 570px; top: 102px; width: 506px;
    font-family: "Audiowide", sans-serif;
    font-size: 74px; line-height: 1; color: var(--maroon);
    white-space: nowrap; text-align: left;
  }
  .band {
    position: absolute; left: 570px; width: 506px;
    background: linear-gradient(90deg, var(--maroon) 0%, var(--maroon-deep) 70%, var(--black) 100%);
    color: var(--white); white-space: nowrap;
    display: flex; align-items: center;
  }
  .band--companies {
    top: 195px; height: 47px;
    font-weight: 400; font-size: 22px; justify-content: space-between;
  }
  .band--companies .sep { padding: 0 8px; }
  .band--web {
    top: 655px; height: 48px;
    font-weight: 600; font-size: 27px; letter-spacing: 0.2px;
  }
  .socials { position: absolute; right: 56px; top: 440px; list-style: none; }
  .social {
    display: flex; align-items: center; justify-content: flex-end;
    height: 50px; margin-bottom: 12px;
    font-weight: 600; font-size: 25px; color: var(--white);
  }
  .social-badge {
    width: 46px; height: 46px; margin-left: 16px; border-radius: 14px;
    background: linear-gradient(135deg, var(--maroon-bright), var(--maroon-deep) 80%);
    display: flex; align-items: center; justify-content: center;
    font-size: 26px; font-weight: 700; color: var(--white);
  }
</style>
</head>
<body>
  <main class="skin">
    <div class="brand">
      <div class="brand-name"><span class="brand-dot"></span>VTK Entertainment</div>
      <p class="brand-tagline">DJ Services | Photo Booths | Event Lighting</p>
    </div>

    <div class="hero-art" role="img" aria-label="Glossy red 3D music note in front of a red equalizer bar pattern"></div>

    <h1 class="owner-name">DoRN HaLE</h1>

    <p class="band band--companies"><span>VTK Entertainment</span><span class="sep">/</span><span>VTK Management</span></p>

    <ul class="socials">
      <li class="social">MrVTK7000<span class="social-badge"></span></li>
      <li class="social">VTKEntertainment<span class="social-badge">#</span></li>
      <li class="social">VTK Entertainment<span class="social-badge"></span></li>
    </ul>

    <p class="band band--web">www.vtkentertainment-example.net</p>
  </main>
</body>
</html>
```